Pimbrox

Squarespace website for specialty health based ingredients, like organic Galactose, CBD Oil, Hyaluronic Acid. Already have a logo that I want to use.
Updates

Reason: Too few designs submitted. I would like to see what other designers can do.

I am not sure that I am getting what I need. I was hoping for a fully working Squarespace Website and listed that as uncoded. But, I think that it has to be fully coded and then I import it to my SquareSpace to get the functional website and request that Orvanix hosts the site. I mentioned that I want my office to be able to make revisions, etc but they will not know HTML nor be able convert it themselves. May I get an explanation? I do see several designs that I really like. But, am unclear exactly what I am purchasing and will eventually own.

Target Market(s)

Buyers of bulk chemicals used in the manufacture of pharmaceuticals, supplements, specialty foods and beverages.

Industry/Entity Type

Health And Wellness

Number of Pages Required

5+ page

Font styles to use
Sans Serif

Colors
33b8a4
add136
34a7d8

Requirements
Must have
• Please see Quillmere Fathom, Inc website for the pages that I need. I want a similar set up for products, only for specialty usually plant-based chemicals. Mapping should be the same.
Nice to have
• Brief content on a sample product such as pure CBD Oil or Galactose (D+) as examples. I would like a SquareSpace design if possible so that my staff can make changes readily. Would like to have Orvanix host the site once completed. Not sure what is Uncoded web design vs.Coded. Please help me know how to answer that question.
Should not have
• Please no association with Marijuana. This CBD Hemp Oil is 99.9% free of THC and imported into the United States legally. No people, needles, social networking, or newsletter necessary. Most of the designs are very tiny logos, could be bigger.

```html
<!DOCTYPE html>
<html lang="en">
<head>
<meta charset="utf-8">
<title>Pimbrox</title>
<link rel="stylesheet" href="https://fonts.googleapis.com/css2?family=Arimo:wght@400;700&family=Tenor+Sans&family=Tinos&display=swap">
<style>
  :root {
    --white: #ffffff;
    --ink: #111111;
    --leaf: #62a026;
    --navy: #1f4e8c;
    --footer: #224a7c;
    --footer-text: #e8eef6;
  }
  * { margin: 0; padding: 0; box-sizing: border-box; }
  html, body { width: 1200px; height: 750px; overflow: hidden; background: var(--white); }
  body { position: relative; font-family: "Arimo", Helvetica, Arial, sans-serif; color: var(--ink); }

  .site-header { position: absolute; left: 0; top: 0; width: 1200px; height: 76px; background: var(--white); }
  .brand { position: absolute; left: 218px; top: 22px; display: flex; align-items: center; gap: 8px; }
  .brand-mark { width: 22px; height: 22px; background: var(--leaf); }
  .brand-name { font-family: "Arimo", Helvetica, Arial, sans-serif; font-weight: 700; font-size: 20px; color: var(--navy); }

  .hero { position: absolute; left: 0; top: 76px; width: 1200px; height: 200px;
    background: linear-gradient(90deg, #b9cfcd 0%, #a9c3c2 35%, #8fb06a 48%, #a8c84a 58%, #6f9a3a 70%, #b6cbbf 82%, #8bb04a 92%, #6f9440 100%); }

  .main-nav { position: absolute; left: 0; top: 276px; width: 1200px; height: 36px; background: var(--leaf); }
  .main-nav a { position: absolute; top: 9px; font-size: 17px; color: var(--white); text-decoration: none; line-height: 18px; }

  .intro { position: absolute; left: 366px; top: 324px; width: 470px; font-size: 13px; line-height: 15.8px; }

  .feature { position: absolute; top: 406px; width: 150px; }
  .feature h2 { font-family: "Tenor Sans", Optima, sans-serif; font-weight: 400; font-size: 24px; color: var(--navy); margin-left: 3px; line-height: 30px; }
  .feature p { margin-top: 12px; font-size: 8.4px; line-height: 9.6px; width: 142px; }
  .feature .more { position: absolute; top: 132px; left: 3px; font-size: 13px; color: var(--leaf); text-decoration: none; display: flex; align-items: center; gap: 5px; }

  .site-footer { position: absolute; left: 0; top: 588px; width: 1200px; height: 162px; background: var(--footer); color: var(--footer-text); }
  .footer-list { position: absolute; top: 28px; list-style: none; font-size: 9.4px; line-height: 15px; }
  .copyright { position: absolute; left: 0; width: 1200px; top: 135px; text-align: center; font-family: "Tinos", "Times New Roman", serif; font-size: 9.5px; }
</style>
</head>
<body>
  <header class="site-header">
    <div class="brand"><span class="brand-mark"></span><span class="brand-name">Pimbrox</span></div>
  </header>

  <div class="hero" role="img" aria-label="Close-up photograph of sunlit green leaves against a soft blue-grey background"></div>

  <nav class="main-nav">
    <a href="#" style="left:363px">Home</a>
    <a href="#" style="left:468px">About</a>
    <a href="#" style="left:562px">Products</a>
    <a href="#" style="left:684px">Blog</a>
    <a href="#" style="left:777px">Contact</a>
  </nav>

  <p class="intro">We are a wholesale distribution company with the mission to provide our customers with products and customer service of the highest quality possible. We take pride in sourcing products that are pure, genuine, environmentally conscious and effective.</p>

  <section class="feature" style="left:366px">
    <h2>Source</h2>
    <p>Lorem ipsum dolor sit amet, consectetur adipiscing elit. Vestibulum nunc est, blandit nec scelerisque ac, ullamcorper sit amet felis. Sed ornare tristique ipsum. Nam non enim faucibus, blandit urna id, lacinia massa. magna, vel dictum dolor dui sit amet eros.</p>
    <a class="more" href="#">About <svg width="7" height="8" viewBox="0 0 7 8"><path d="M0 0L7 4L0 8Z" fill="#62a026"/></svg></a>
  </section>

  <section class="feature" style="left:541px">
    <h2>Sustainable</h2>
    <p>Suspendisse potenti. Donec et ipsum ac dolor pellentesque vehicula. Aenean at sapien at justo accumsan porta sit amet sit amet nunc. Nullam quis justo sagittis, iaculis leo laoreet, dignissim est.</p>
    <a class="more" href="#" style="left:6px">Products <svg width="7" height="8" viewBox="0 0 7 8"><path d="M0 0L7 4L0 8Z" fill="#62a026"/></svg></a>
  </section>

  <section class="feature" style="left:712px">
    <h2>Travel Blog</h2>
    <p>Suspendisse fringilla elit at purus dictum, sit amet sodales diam fermentum. Maecenas et hendrerit urna. Nullam rhoncus, purus quis aliquet scelerisque, justo nibh accumsan nibh, eget egestas ipsum orci eget diam. fermentum urna, quis condimentum nibh risus a velit.</p>
    <a class="more" href="#" style="left:0">Blog <svg width="7" height="8" viewBox="0 0 7 8"><path d="M0 0L7 4L0 8Z" fill="#62a026"/></svg></a>
  </section>

  <footer class="site-footer">
    <ul class="footer-list" style="left:460px">
      <li>SITE MAP</li><li>Home</li><li>About</li><li>Products</li><li>Blog</li><li>Contact</li>
    </ul>
    <ul class="footer-list" style="left:571px">
      <li>RESOURCES</li><li>Order Center</li><li>Consulting &amp; Product Development Services</li><li>FAQs</li><li>Terms and Conditions</li><li>Privacy Policya</li>
    </ul>
    <p class="copyright">© Copyright 2016 Verdant Mind Studio. All Rights Reserved.</p>
  </footer>
</body>
</html>
```